Für das neue Tantra-Bildungszetrum: 8-oder 10-Seiten-Faltblatt und ein Plakat DIN A3
Zielgruppe
Es geht darum, über das Angebot des neuen Bildungszentrums Kreis der Morgenröte zu informieren.
Das Zentrum organisiert und führt regelmäßige Veranstaltungen wie Info-Vorträge, Schnuppertage, Seminare, Kurse und Intensivtrainings durch, ist in allem spezialisiert auf Tantra. Das Zentrum ist vertreten an mehreren Standorten Deutschlands durch das jeweils ein Team an Lehrern und Dozenten. Für die Veranstaltungen werden externe Räume angemietet. Das Angebot soll in jeder Stadt, wo die Broschüren oder Faltblätter verteilt werden. Die Anmeldung und Registrierung erfolgt über die neue Homepage, die bald freigegeben wird und noch nicht zur Verfügung steht.
Das Besondere am Zentrum ist die Möglichkeit, eigene tantrische Selbsterfahrungen zu machen und entweder später oder als Option sich gleich für einen der sechs neuen Tantra- Ausbildungsberufe zu entscheiden.
Darüber hinaus, soll die Broschüre oder die Faltblätter zur Mitarbeit und Kooperation mit selbständigen Yoga- und Tantra-Lehrern, sowie Ärzten, Therapeuten und Heilpraktiken einladen.
Das Bildungszentrum ist ein Netzwerk der Honorar-Dozenten, die entweder Lehrer und Experte auf dem tantrischen Bereich oder Vertreter der klassischen und alternativen Heilkunde oder beides zusammen sind.
Wer ist die Zielgruppe? Männer und Frauen, vom 18 - 60 Jahre. Menschen, die sich für Tantra und Selbsterfahrung interessieren, und Menschen, die nach einer neuen beruflichen Perspektive suchen.
Aufgabenstellung
1). 10-Seiten- Faltblatt designen
2). Plakat DIN A3 gestalten

```html
<!DOCTYPE html>
<html lang="de">
<head>
<meta charset="utf-8">
<title>Kreis der Morgenröte – Plakat</title>
<link href="https://fonts.googleapis.com/css2?family=Jost:wght@400;500;600&family=Merriweather:wght@700&family=Kaushan+Script&display=swap" rel="stylesheet">
<style>
  :root{
    --backdrop:#c9673f;
    --teal:#1c6a6a;
    --saffron:#e6bf5c;
    --orange:#ef8a3c;
    --coral:#e8714a;
    --ink:#1f5f60;
    --white:#ffffff;
  }
  *{box-sizing:border-box;margin:0;padding:0}
  html,body{width:1200px;height:1062px;overflow:hidden}
  body{background:var(--backdrop);font-family:"Jost",sans-serif;color:var(--ink)}
  .poster{position:absolute;left:255px;top:43px;width:690px;height:976px;background:var(--white)}
  .poster__field{position:absolute;left:0;top:0;width:690px;height:817px;background:var(--teal)}
  .panel{position:absolute;left:30px;top:26px;width:628px;height:763px;background:var(--saffron)}
  .panel p,.panel li{font-size:9.6px;line-height:13.7px;hyphens:auto}
  .brand{position:absolute;left:22px;top:22px;display:flex;align-items:center;gap:8px;font-family:"Merriweather",serif;font-weight:700;color:var(--ink)}
  .brand__dot{width:34px;height:34px;border-radius:50%;background:var(--orange);flex:none}
  .brand__text{font-size:17px;line-height:22px}
  .brand__name{display:block;font-size:23px;line-height:28px}
  .col-left{position:absolute;left:22px;top:114px;width:288px}
  .cities{position:absolute;left:22px;top:334px;width:288px;font-weight:600}
  .invite{position:absolute;left:80px;top:370px;width:230px}
  .invite p{margin-bottom:5px}
  .script{font-family:"Kaushan Script",cursive;color:var(--coral)}
  .career-head{position:absolute;left:22px;top:448px;font-size:15px}
  .career-intro{position:absolute;left:80px;top:478px;width:232px;font-weight:600}
  .careers{position:absolute;left:38px;top:536px;list-style:none}
  .careers li{display:flex;align-items:center;height:30.5px;font-weight:600;font-size:9.8px}
  .careers__mark{width:22px;height:22px;border-radius:50%;border:1.5px solid var(--orange);margin-right:20px;opacity:.8}
  .lead{position:absolute;left:321px;top:24px;width:292px;font-size:15.5px;line-height:19.5px}
  .offer{position:absolute;left:321px;width:292px}
  .offer p{margin-bottom:5px}
  .offer--courses{top:114px}
  .offer--year{top:448px}
  .offer--retreat{top:612px}
  .offer--retreat p{font-weight:600}
  .badge{float:left;width:64px;height:64px;border-radius:50%;background:var(--orange);margin:4px 12px 4px 0;display:flex;align-items:center;justify-content:center;text-align:center;color:var(--saffron);font-size:8.5px;line-height:9.5px;font-weight:600}
  .footer{position:absolute;left:0;top:817px;width:690px;height:159px}
  .portrait{position:absolute;left:30px;top:14px;width:126px;height:115px;background:linear-gradient(160deg,#b8a48a,#5a4a3e 60%,#2b2623)}
  .caption{position:absolute;left:30px;top:135px;font-size:6.5px;color:var(--orange);font-weight:500}
  .emblem{position:absolute;left:214px;top:25px;width:93px;height:90px;border-radius:50%;background:radial-gradient(circle,#fbe3cf,#f6c39b)}
  .contact{position:absolute;left:351px;top:25px;font-size:11.5px;line-height:20.5px}
  .contact dl{display:grid;grid-template-columns:58px auto}
  .contact dt{font-weight:400}
  .contact dd{font-weight:600}
  .contact p{font-weight:600}
</style>
</head>
<body>
<main class="poster">
  <section class="poster__field">
    <div class="panel">
      <header class="brand">
        <span class="brand__dot"></span>
        <span class="brand__text">Bildungszentrum<span class="brand__name">Kreis der Morgenröte</span></span>
      </header>

      <p class="col-left">Unser Bildungszentrum soll viele Menschen bei ihren inneren Transformationsprozessen unterstützen indem es spezielle berufliche Perspektiven anbietet, bei denen Selbstverwirklichung in authentischem Kontakt mit anderen Menschen möglich ist. Wenn die innere Welt in Frieden, Harmonie und Ruhe ist, so wird sich dies auch auf unsere äußere Welt auswirken und initiiert so einen Gesellschaftwandel durch innere Transformation. Tantra liefert uns Techniken, die unser Bewusstsein durch die Transformation innerer Vorgänge grundlegend wandeln. Tantra unterstützt Menschen in ihrem Bemühen um Selbstverwirklichung, spirituelles Wachstum, innere Entwicklung sowie der Verbesserung ihrer Liebes- und Lustfähigkeit. Es fördert das Aufblühen der eigenen inneren Göttlichkeit und das Nutzen von sexueller Energie im spirituellen Sinne. Dies ist nur kleiner Ausschnitt dessen, was Tantra uns ermöglicht.</p>

      <p class="cities">Für unsere Angebote mieten wir geeignete Räume in Berlin, Leipzig, Hamburg, Dresden und bald in deiner Stadt.</p>

      <div class="invite">
        <p>Wir laden dich herzlich zu unseren regelmäßigen Vorträgen ein:</p>
        <p>1. Was ist Tantra?</p>
        <p>2. Berufliche Perspektiven mit Tantra.</p>
      </div>

      <h2 class="script career-head">Mach Tantra zu deinem Beruf!</h2>
      <p class="career-intro">Investiere zwei bis fünf wundervolle Jahre je nach deiner Wahl in eine Berufsausbildung mit Zukunft! Welche unserer sechs Ausbildungsberufe spricht dich an?</p>
      <ul class="careers">
        <li><span class="careers__mark"></span>1. Tantra-Lehrer</li>
        <li><span class="careers__mark"></span>2. Tantra-Yoga-Lehrer</li>
        <li><span class="careers__mark"></span>3. Tantrischer Massagetherapeut</li>
        <li><span class="careers__mark"></span>4. Tantrischer Sexualtherapeut</li>
        <li><span class="careers__mark"></span>5. Tantra-Coach</li>
        <li><span class="careers__mark"></span>6. Selbst Ausbilder werden</li>
      </ul>

      <h2 class="script lead">Erfahre den Geschmack, den Geruch, die Farbe und den Klang von Tantra bei einem unserer Schnuppertage oder Einsteiger-Wochenenden.</h2>

      <article class="offer offer--courses">
        <span class="badge">12<br>Wochen<br>Kurse</span>
        <p>Steige ein in den nächsten Tantra-Kurs, je nach deinem Level und Vorerfahrungen. Jeden Monat außer der Sommerpause (Juli - August) beginnt ein neuer Kurs. Diese Kurse helfen dir in die Gruppe mit Menschen zu kommen, die auf deinem Level sind und dienen deiner kontinuirlichen Praxis. Melde dich an für:</p>
        <p>12- Wochen Kurs „Tantra für Anfänger“, wenn du ganz neu und unerfahren bist, oder um in deine tantrische Praxis wieder einzusteigen. Im Kurs bleibst du angezogen. Der Fokus liegt auf der Entwicklung der Selbstwahrnehmung und dem Erlernen Basis-Techniken.</p>
        <p>12- Wochen Kurs „Tantra für Mittelstufe“, wenn du mit den Grund-Atemtechniken, Meditations- und Visualisierungsübungen vertraut bist. Im Kurs werden wir teils angezogen, teil bewusst nackt sein.</p>
        <p>12- Wochen Kurs „Tantra für Fortgeschrittene“, wenn du sehr vertraut mit den tantrischen Techniken bist, dich natürlich und selbstsicher nackt in der Gruppe fühlen kannst. In diesem Kurs geht es um das Erlernen und Nutzen der tantrischen sexuellen Praktiken. Es finden keine sexuelle Interaktionen statt. Übung der Techniken findet nicht im Rahmen des Kurses statt.</p>
      </article>

      <article class="offer offer--year">
        <span class="badge">Jahres<br>training</span>
        <p>Im Jahrestraining gehst du mit zehn intensiven verlängerten Wochenenden in die Erfahrung ausgedehnter tantrischer sexueller Praxis. Die Gruppe derer, die unser Jahrestraining absolvieren, trifft sich zu zehn Terminen für jeweils ein verlängertes Wochenende von Freitag bis Sonntag. Während unseres Jahrestrainings erlebst du die intensive Beschäftigung mit tantrischen Techniken, die verstärkt ihren Fokus auf tantrischer sexueller Praxis hat. Die zehn Treffen des Jahrestrainings stellen eine intensive Selbsterfahrung mit transformierendem Charakter dar.</p>
      </article>

      <article class="offer offer--retreat">
        <span class="badge">Tantra<br>Retreats</span>
        <p>Tantra Retreats – intensive Erfahrungen der Innenwelt Möchtest du dich innerhalb von kurzer Zeit sehr intensiv erkennen und erfahren? Wenn ja, dann ist ein Tantra Retreat genau das Richtige für dich. Über mehrere Tage hinweg wirst du in die Welt der Gefühle, des Bewusstseins und der Liebe eintauchen. Du legst für die Zeit des Retreats alle deine im Außen liegenden Verpflichtungen ab und widmest dich deinem Inneren. Diese Tage des tantrischen Rückzugs ermöglichen einen weitgreifenden inneren Wandel bei jedem Einzelnen der Gruppe.</p>
      </article>
    </div>
  </section>

  <footer class="footer">
    <div class="portrait" role="img" aria-label="Porträtfoto der Gründerin vor Statuen"></div>
    <p class="caption">Miralda - Gründerin des Bildungszentrums</p>
    <div class="emblem" role="img" aria-label="Chakra-Ornament in Orange"></div>
    <div class="contact">
      <dl>
        <dt>Kontakt:</dt><dd>www.kreis-morgenroete.de</dd>
        <dt>Telefon:</dt><dd>0176 52 17 38 04</dd>
        <dt>FB:</dt><dd>Tantrisches.Bildungszentrum.KreisDerMorgenroete</dd>
        <dt>Twitter:</dt><dd>/KreisDerMorgenroete</dd>
      </dl>
      <p>Wir sind ein wachsendes Netzwerk aus mehreren Lehrern.</p>
    </div>
  </footer>
</main>
</body>
</html>
```